Website for a new t-shirt company called wrendusktees.com

We are looking for a talented web designer to create a website that aligns with our brand's message and identity centered around the theme of "Wren Dusk." The website should be modern, clean, and visually appealing while also being user-friendly and easy to navigate.

We will be using the Big Commerce platform for our online store section, so the designer should have experience in designing websites on this platform.

We would like the website to have the following elements:

A color scheme that aligns with the brand's identity and message
A homepage that showcases our products and message, with clear calls-to-action for visitors to explore further
A blog section that highlights our brand's philosophy and offers advice and tips for people looking to make positive changes in their lives
An "About Us" section that introduces our brand and team and offers insight into our mission and values
A contact form that allows visitors to easily get in touch with us for inquiries or support
We are open to creative suggestions and ideas from the designer, but we would like the website to have a modern and minimalist aesthetic that resonates with our target audience of 20 to 40-year-olds.

```html
<!DOCTYPE html>
<html lang="en">
<head>
<meta charset="utf-8">
<title>Wren Dusk — T-Shirts</title>
<link href="https://fonts.googleapis.com/css2?family=Jost:wght@400;500;600;700&display=swap" rel="stylesheet">
<style>
:root{
  --ink:#111;
  --white:#fff;
  --hero-bg:#ececec;
  --card-inner:#dcdcdc;
  --footer-bg:#f4f4f4;
  --muted:#444;
  --line:#d9d9d9;
}
*{margin:0;padding:0;box-sizing:border-box}
html,body{width:1200px;height:3585px;overflow:hidden}
body{position:relative;background:var(--white);color:var(--ink);font-family:"Jost",Arial,sans-serif}
.abs{position:absolute}
.promo-bar{left:0;top:0;width:1200px;height:50px;background:var(--ink);color:var(--white);font:500 14px "Jost",sans-serif;display:flex;align-items:center;justify-content:center}
.site-nav{left:0;top:50px;width:1200px;height:85px;background:var(--white)}
.brand{left:118px;top:24px;font:600 32px "Jost",sans-serif;letter-spacing:1px}
.menu{left:448px;top:36px;display:flex;gap:61px;font:400 14px "Jost",sans-serif}
.nav-tools{left:996px;top:33px;display:flex;gap:14px;align-items:center;border-left:1px solid var(--ink);padding-left:14px;height:20px}
.hero{left:0;top:135px;width:1200px;height:514px;background:var(--hero-bg)}
.hero-kicker{left:110px;top:114px;font:600 16px "Jost",sans-serif}
.hero-title{left:108px;top:140px;font:600 92px/1 "Jost",sans-serif}
.hero-text{left:110px;top:278px;width:500px;font:15px/25px Arial,sans-serif;color:#333}
.btn-dark{background:var(--ink);color:var(--white);font:600 15px "Jost",sans-serif;display:flex;align-items:center;justify-content:center;border-radius:3px}
.btn-light{background:var(--white);color:var(--ink);font:600 14px "Jost",sans-serif;display:flex;align-items:center;justify-content:center;border-radius:3px}
.dots{left:112px;top:454px;display:flex;gap:6px}
.dots span{width:14px;height:14px;border-radius:50%;background:var(--white)}
.dots span.on{background:var(--ink)}
.photo-card{background:var(--white);padding:8px;border-radius:10px;box-shadow:0 4px 14px rgba(0,0,0,.18)}
.photo-card div{width:100%;height:100%;border-radius:6px}
.section-title{left:0;width:1200px;text-align:center;font:600 34px "Jost",sans-serif;letter-spacing:.5px}
.product{top:807px;width:234px;height:307px;border:9px solid var(--ink);border-radius:24px;padding:8px;background:var(--white)}
.product-inner{width:100%;height:100%;background:var(--card-inner);border-radius:14px;position:relative}
.product-shirt{position:absolute;left:30px;top:20px;width:142px;height:160px}
.product-tag{position:absolute;left:0;width:100%;top:206px;text-align:center;font:500 10px "Jost",sans-serif}
.product-name{position:absolute;left:0;width:100%;top:222px;text-align:center;font:600 18px "Jost",sans-serif}
.feature{top:1192px;width:471px;height:278px;border-radius:8px;overflow:hidden;color:var(--white)}
.feature h3{position:absolute;left:22px;top:40px;font:600 34px "Jost",sans-serif}
.feature p{position:absolute;left:26px;top:94px;width:420px;font:14px/24.5px Arial,sans-serif}
.about-band{left:0;top:1551px;width:1200px;height:317px;color:var(--white);text-align:center}
.member-photo{top:2017px;width:227px;height:263px;border-radius:10px}
.member-name{top:2296px;width:227px;text-align:center;font:500 17px "Jost",sans-serif}
.member-role{top:2324px;width:227px;text-align:center;font:14px "Jost",sans-serif}
.member-social{top:2356px;width:227px;display:flex;justify-content:center;gap:5px}
.member-social span{width:19px;height:19px;border-radius:50%;background:var(--ink)}
.post-img{top:2561px;width:227px;height:223px;border-radius:10px}
.post-title{top:2800px;width:200px;font:600 16px/21px "Jost",sans-serif}
.post-text{top:2851px;width:205px;font:12px/21.5px "Jost",sans-serif;color:#222}
.post-link{top:2940px;font:11px "Jost",sans-serif;text-decoration:underline;color:#555}
.footer{left:0;top:3060px;width:1200px;height:525px;background:var(--footer-bg)}
.foot-col h4{font:500 21px "Jost",sans-serif;margin-bottom:14px;white-space:nowrap}
.foot-col li{list-style:none;font:14px/30px "Jost",sans-serif;color:var(--muted)}
.foot-col.caps li{font-size:12px}
.field{border:1px solid #555;border-radius:6px;font:13px "Jost",sans-serif;color:#555;padding:10px 20px;background:var(--footer-bg)}
.divider{left:110px;top:3470px;width:980px;height:1px;background:var(--line)}
.copyright{left:116px;top:3512px;font:15px "Jost",sans-serif}
.pay{top:3508px;left:816px;display:flex;gap:6px}
.pay span{width:50px;height:32px;background:var(--white);border:1px solid var(--line);border-radius:4px;font:600 10px "Jost",sans-serif;display:flex;align-items:center;justify-content:center}
</style>
</head>
<body>

<div class="abs promo-bar">50% OFF WITH THE CODE WELCOME1!</div>

<header class="abs site-nav">
  <div class="abs brand">Wren Dusk</div>
  <nav class="abs menu"><span>HOME</span><span>SHOP</span><span>OUR BLOG</span><span>ABOUT</span><span>CONTACT</span></nav>
  <div class="abs nav-tools">
    <svg width="14" height="14" viewBox="0 0 14 14"><circle cx="6" cy="6" r="4.5" fill="none" stroke="#111" stroke-width="2"/><line x1="9" y1="9" x2="13" y2="13" stroke="#111" stroke-width="2"/></svg>
    <svg width="13" height="14" viewBox="0 0 13 14"><circle cx="6.5" cy="4" r="3.5" fill="#111"/><path d="M0 14c0-4 3-6 6.5-6s6.5 2 6.5 6z" fill="#111"/></svg>
    <svg width="15" height="14" viewBox="0 0 15 14"><path d="M0 1h3l2 8h8l2-6H4" fill="none" stroke="#111" stroke-width="2"/><circle cx="6" cy="12" r="1.5" fill="#111"/><circle cx="12" cy="12" r="1.5" fill="#111"/></svg>
  </div>
</header>

<section class="abs hero">
  <div class="abs hero-kicker">WELCOME TO</div>
  <div class="abs hero-title">Wren Dusk</div>
  <p class="abs hero-text">Lorem ipsum dolor sit amet, consectetur adipiscing elit, sed do eiusmod tempor incididunt ut labore et dolore magna aliqua.</p>
  <div class="abs btn-dark" style="left:110px;top:351px;width:143px;height:47px">Shop Now</div>
  <div class="abs dots"><span></span><span class="on"></span><span></span></div>

  <div class="abs photo-card" style="left:628px;top:90px;width:204px;height:286px;transform:rotate(-9deg)">
    <div role="img" aria-label="Man in a black t-shirt on a city street at night" style="background:linear-gradient(160deg,#6b5a48,#1e1e1e)"></div>
  </div>
  <div class="abs photo-card" style="left:872px;top:92px;width:204px;height:286px;transform:rotate(9deg)">
    <div role="img" aria-label="Woman in a white t-shirt outdoors" style="background:linear-gradient(160deg,#8a7052,#e8e6e8)"></div>
  </div>
  <div class="abs photo-card" style="left:750px;top:155px;width:208px;height:275px">
    <div role="img" aria-label="Smiling man in sunglasses wearing a white t-shirt" style="background:linear-gradient(180deg,#9a9a9a,#dedede)"></div>
  </div>
</section>

<h2 class="abs section-title" style="top:718px">OUR PRODUCTS</h2>

<div class="abs product" style="left:110px"><div class="product-inner">
  <div class="product-shirt" role="img" aria-label="Black t-shirt" style="background:#000;border-radius:16px 16px 6px 6px"></div>
  <div class="product-tag">MOST POPULAR</div><div class="product-name">WREN DUSK TSHIRT</div></div></div>
<div class="abs product" style="left:358px"><div class="product-inner">
  <div class="product-shirt" role="img" aria-label="Light grey sweatshirt" style="background:#efefef;border-radius:16px 16px 6px 6px"></div>
  <div class="product-tag">MOST POPULAR</div><div class="product-name">WREN DUSK TSHIRT</div></div></div>
<div class="abs product" style="left:606px"><div class="product-inner">
  <div class="product-shirt" role="img" aria-label="Sky blue t-shirt" style="background:#7cbfdd;border-radius:16px 16px 6px 6px"></div>
  <div class="product-tag">MOST POPULAR</div><div class="product-name">WREN DUSK TSHIRT</div></div></div>
<div class="abs product" style="left:854px"><div class="product-inner">
  <div class="product-shirt" role="img" aria-label="Sand beige t-shirt" style="background:#d8cdb8;border-radius:16px 16px 6px 6px"></div>
  <div class="product-tag">MOST POPULAR</div><div class="product-name">WREN DUSK TSHIRT</div></div></div>

<div class="abs feature" style="left:111px" role="img" aria-label="Man in a white t-shirt leaning on a concrete wall">
  <div style="position:absolute;inset:0;background:linear-gradient(135deg,#8b857d,#55524d 60%,#6e6c68)"></div>
  <h3>OUR MISSION</h3>
  <p>Lorem ipsum dolor sit amet, consectetur adipiscing elit, sed do eiusmod tempor incididunt ut labore et dolore magna aliqua. Quis ipsum suspendisse ultrices gravida.</p>
  <div class="abs btn-light" style="left:26px;top:190px;width:135px;height:44px">Shop Now</div>
</div>
<div class="abs feature" style="left:619px" role="img" aria-label="Close-up of a grey t-shirt on a model">
  <div style="position:absolute;inset:0;background:linear-gradient(135deg,#6e6259,#9b928a 55%,#5e5650)"></div>
  <h3 style="left:28px">VALUES</h3>
  <p>Lorem ipsum dolor sit amet, consectetur adipiscing elit, sed do eiusmod tempor incididunt ut labore et dolore magna aliqua. Quis ipsum suspendisse ultrices gravida.</p>
  <div class="abs btn-light" style="left:26px;top:190px;width:135px;height:44px">Shop Now</div>
</div>

<section class="abs about-band" role="img" aria-label="Man in sunglasses and a white t-shirt on a blurred city street">
  <div style="position:absolute;inset:0;background:linear-gradient(90deg,#6f6b66,#8d8276 50%,#5d554e)"></div>
  <h2 style="position:absolute;left:0;width:1200px;top:65px;font:600 34px 'Jost',sans-serif">ABOUT</h2>
  <p style="position:absolute;left:300px;width:600px;top:116px;font:14px/25px Arial,sans-serif">Lorem ipsum dolor sit amet, consectetur adipiscing elit, sed do eiusmod tempor incididunt ut labore et dolore magna aliqua. Quis ipsum suspendisse ultrices gravida.</p>
  <div class="abs btn-light" style="left:532px;top:198px;width:136px;height:45px">Shop Now</div>
</section>

<h2 class="abs section-title" style="top:1940px">OUR TEAM</h2>

<div class="abs member-photo" style="left:111px;background:linear-gradient(180deg,#c9c6c1,#e8e6e6)" role="img" aria-label="Portrait of a team member"></div>
<div class="abs member-photo" style="left:361px;background:linear-gradient(180deg,#8c8c8a,#c6bdb3)" role="img" aria-label="Portrait of a team member"></div>
<div class="abs member-photo" style="left:612px;background:linear-gradient(180deg,#b8b1aa,#3ab0d6)" role="img" aria-label="Portrait of a team member"></div>
<div class="abs member-photo" style="left:862px;background:linear-gradient(180deg,#eeeeef,#e7dcd0)" role="img" aria-label="Portrait of a team member"></div>

<div class="abs member-name" style="left:111px">Milo Harrington</div>
<div class="abs member-name" style="left:361px">Sera Lindqvist</div>
<div class="abs member-name" style="left:612px">Tomas Reyel</div>
<div class="abs member-name" style="left:862px">Juna Marlowe</div>
<div class="abs member-role" style="left:111px">Lorem Ipsum</div>
<div class="abs member-role" style="left:361px">Lorem Ipsum</div>
<div class="abs member-role" style="left:612px">Lorem Ipsum</div>
<div class="abs member-role" style="left:862px">Lorem Ipsum</div>
<div class="abs member-social" style="left:111px"><span></span><span></span><span></span><span></span></div>
<div class="abs member-social" style="left:361px"><span></span><span></span><span></span><span></span></div>
<div class="abs member-social" style="left:612px"><span></span><span></span><span></span><span></span></div>
<div class="abs member-social" style="left:862px"><span></span><span></span><span></span><span></span></div>

<h2 class="abs section-title" style="top:2484px">OUR BLOG</h2>

<div class="abs post-img" style="left:111px;background:linear-gradient(180deg,#a89f95,#e9e8e6)" role="img" aria-label="Man in a white t-shirt on a street"></div>
<div class="abs post-img" style="left:361px;background:linear-gradient(180deg,#6d5440,#3c4a66)" role="img" aria-label="Woman in a white t-shirt at a café table"></div>
<div class="abs post-img" style="left:610px;background:linear-gradient(180deg,#9c9ea1,#ececec)" role="img" aria-label="Back of a man wearing a white printed t-shirt"></div>
<div class="abs post-img" style="left:859px;background:linear-gradient(180deg,#f0a070,#f0eeec)" role="img" aria-label="Woman in an orange hoodie seated on a chair"></div>

<div class="abs post-title" style="left:120px">Lorem ipsum dolor sit amet, consectetur</div>
<div class="abs post-title" style="left:369px">Lorem ipsum dolor sit amet, consectetur</div>
<div class="abs post-title" style="left:618px">Lorem ipsum dolor sit amet, consectetur</div>
<div class="abs post-title" style="left:867px">Lorem ipsum dolor sit amet, consectetur</div>
<p class="abs post-text" style="left:120px">Lorem ipsum dolor sit amet, consectetur adipiscing elit, sed do eiusmod tempor incididunt ut labore et dolore magna aliqua.</p>
<p class="abs post-text" style="left:369px">Lorem ipsum dolor sit amet, consectetur adipiscing elit, sed do eiusmod tempor incididunt ut labore et dolore magna aliqua.</p>
<p class="abs post-text" style="left:618px">Lorem ipsum dolor sit amet, consectetur adipiscing elit, sed do eiusmod tempor incididunt ut labore et dolore magna aliqua.</p>
<p class="abs post-text" style="left:867px">Lorem ipsum dolor sit amet, consectetur adipiscing elit, sed do eiusmod tempor incididunt ut labore et dolore magna aliqua.</p>
<div class="abs post-link" style="left:120px">Learn More</div>
<div class="abs post-link" style="left:369px">Learn More</div>
<div class="abs post-link" style="left:618px">Learn More</div>
<div class="abs post-link" style="left:867px">Learn More</div>

<footer class="abs footer">
  <div class="abs foot-col caps" style="left:108px;top:58px"><h4>QUICK LINKS</h4><ul><li>HOME</li><li>SHOP</li><li>OUR BLOG</li><li>ABOUT</li><li>CONTACT</li></ul></div>
  <div class="abs foot-col" style="left:270px;top:58px"><h4>POPULAR BRANDS</h4><ul><li>Lorem ipsum dolor</li><li>Lorem ipsum dolor</li><li>Lorem ipsum</li><li>Lorem ipsum dolor</li><li>Lorem ipsum dolor</li></ul></div>
  <div class="abs foot-col" style="left:482px;top:58px"><h4>CUSTOMER INFO</h4><ul><li>Contact Us</li><li>FAQs</li><li>Returns</li><li>Privacy Policy</li><li>Terms &amp; Conditions</li><li>Terms of Services</li><li>Refund policy</li></ul></div>
  <div class="abs foot-col" style="left:692px;top:58px"><h4>GET IN TOUCH</h4></div>
  <div class="abs field" style="left:690px;top:110px;width:191px;height:43px">First Name</div>
  <div class="abs field" style="left:892px;top:110px;width:192px;height:43px">Last Name</div>
  <div class="abs field" style="left:690px;top:165px;width:191px;height:42px">Phone</div>
  <div class="abs field" style="left:892px;top:165px;width:192px;height:42px">Email</div>
  <div class="abs field" style="left:690px;top:221px;width:393px;height:75px">Phone</div>
  <div class="abs btn-dark" style="left:690px;top:310px;width:133px;height:48px;border-radius:4px">SUBMIT</div>
</footer>

<div class="abs divider"></div>
<div class="abs copyright">©Copyrights 2023 Wren Dusk &nbsp;| &nbsp;&nbsp;All Rights Reserved</div>
<div class="abs pay"><span>Zelvaro</span><span>Mintrel</span><span>Korvex</span><span>Plindo</span><span>Tessup</span></div>

</body>
</html>
```